Kestavo Estates is a commercial real estate development company based in the United States. We develop high-end office buildings and student housing apartments. We have a new logo and need to update all of our stationary items and business cards. We would like the design to be clean and professional. Our logo and color information is attached. Our logo MUST be in full color and not as white. It is preferred that the logo is on a white background.

Color code Blue R 0. G 62. B 124 ( #003E7C )
C 100 M84 Y 26 K 22
Black R32. G30. B30 ( #201E1E)
C100 M100 Y100 K100

Font used TRAJAN PRO3 PRO BOLD.

Items needed:
1. Business card - Leaning towards doing just a one side business card in a thicker paper. Include - logo, name - Peter T. Vance, Title - Chairman & CEO, 1870 Pembrook Blvd. Suite 400, Atlanta, GA 30127 - Cell number 404.555.####, Office 770.555.02## email@kestavoestates.com; www.kestavoestates.com.

2. Letterhead - Standard 8.5 by 11 paper. We do have a smaller size for the CEO that is 7.25 by 10.5 that is just a mirror of the letterhead except with his name (Peter T. Vance) and title (Chariman & CEO) listed at the top in the header. Letthead needs address, phone number and website, plus logo. *Prepared such that we can either implement as a Google Document template or professionally print.

3. Legal sized envelope - #10 envelope - which measures 4 1/8" by 9 1/2". We also use the same size envelope with a window. Need logo and address. A photo of the old envelope style is attached.

4. 9" x 12" Pocket folder - Need a design that can also be split to be a cover page and back - We use the cover pages in spiral binding machine, so we need to leave room on the left for that. One of the pockets should hold a business card. Include logo, address, phone, website. Also if text is needed, we could say development / leasing / property management.

5. Shipping label - 3 1/3" x 4" inches and 6 per page. Just need logo and address listed at top of the label and white space at bottom.

Company: Kestavo Estates
Address: 1870 Pembrook Blvd. Suite 400, Atlanta, GA 30127
Phone: 770.555.0214
Fax: 770.555.0287 (probably not needed)
Website: www.kestavoestates.com

Thank you for all your help!

Target Market(s)

Should communicate a strong corporate feel

Contact Information for Business Card

Include - logo, name - Peter T. Vance, Title - Chairman & CEO, 1870 Pembrook Blvd. Suite 400, Atlanta, GA 30127 - Cell number 404.555.####, Office 770.555.02## email@kestavoestates.com; www.kestavoestates.com.

Logo Text

Kestavo Estates

Colors

Requirements
Must have
• Our logo MUST be in full color and not as white. It is preferred that the logo is on a white background.
• Colors - Color code Blue R 0. G 62. B 124 ( #003E7C )
• C 100 M84 Y 26 K 22
Nice to have
• Font used in logo TRAJAN PRO3 PRO BOLD. Would love to see options of both a one sided and double-sided.
Should not have
• Logo in white.

```html
<!DOCTYPE html>
<html lang="en">
<head>
<meta charset="utf-8">
<title>Kestavo Estates – Stationery Set</title>
<link href="https://fonts.googleapis.com/css2?family=Cinzel:wght@700&family=Open+Sans:wght@400;600;700&display=swap" rel="stylesheet">
<style>
:root{
  --brand-blue:#003e7c;
  --brand-black:#201e1e;
  --paper:#ffffff;
  --stage:#eceef1;
  --ghost:#e6e9ee;
  --rule:#c9ced6;
  --body-text:#2b2929;
}
*{margin:0;padding:0;box-sizing:border-box}
html,body{width:1200px;height:3511px;overflow:hidden}
body{background:var(--stage);position:relative;font-family:"Open Sans",Arial,sans-serif;color:var(--brand-black)}
.sheet{position:absolute;background:var(--paper);box-shadow:0 4px 18px rgba(0,0,0,.12)}

/* wordmark */
.wordmark{display:flex;align-items:center;gap:10px;color:var(--brand-blue);font-family:"Cinzel",Georgia,serif;font-weight:700;line-height:1}
.wordmark .dot{border-radius:50%;background:var(--brand-blue);flex:none}
.wordmark .lines{display:flex;flex-direction:column}
.wordmark .top{letter-spacing:.02em}
.wordmark .bottom{letter-spacing:.28em}

.ghost-ring{position:absolute;border-radius:50%;border:34px solid var(--ghost)}

/* letterhead */
.letterhead-back{left:60px;top:53px;width:540px;height:751px}
.letterhead-front{left:636px;top:53px;width:528px;height:751px}
.lh-header{position:absolute;left:26px;right:26px;top:22px;height:44px;display:flex;justify-content:space-between;align-items:center;border-bottom:3px solid var(--brand-blue);padding-bottom:8px}
.lh-person{text-align:right;color:var(--brand-blue)}
.lh-person .name{font-weight:700;font-size:15px}
.lh-person .title{font-size:10px;color:var(--brand-black)}
.lh-body{position:absolute;left:44px;right:44px;top:130px;font-size:11.2px;line-height:1.42;color:var(--body-text)}
.lh-footer{position:absolute;left:0;right:0;bottom:20px;text-align:center;font-size:8px;color:var(--brand-blue);line-height:1.5}
.lh-footer strong{font-weight:700}
.band{position:absolute;left:0;right:0;bottom:0;height:8px;background:var(--brand-blue)}
.band-stripes{position:absolute;right:10px;bottom:8px;display:flex;gap:5px}
.band-stripes i{display:block;width:14px;height:6px;background:var(--brand-blue);transform:skewX(-40deg)}

/* business cards */
.card{width:480px;height:274px;top:1140px}
.card-front{left:80px;display:flex;align-items:center;justify-content:center;overflow:hidden}
.card-back{left:640px;padding:30px 34px}
.card-name{font-size:24px;font-weight:700;color:var(--brand-blue)}
.card-title{font-size:13px;margin-bottom:18px}
.contact-row{display:flex;align-items:center;gap:12px;font-size:13px;margin-bottom:9px}
.icon{width:20px;height:20px;background:var(--brand-blue);border-radius:3px;flex:none}

/* envelopes */
.envelope-back{left:96px;top:1776px;width:1008px;height:516px;overflow:hidden}
.envelope-back svg{position:absolute;inset:0}
.envelope-front{left:96px;top:2460px;width:1008px;height:300px}
.env-return{position:absolute;left:34px;top:40px}
.env-address{font-size:15px;margin-top:14px;line-height:1.3}
.envelope-front .band{height:14px}
.envelope-front .band-stripes{bottom:14px;right:16px}
.envelope-front .band-stripes i{width:22px;height:10px}

/* labels */
.label{top:2976px;width:564px;height:506px;border:2px solid #8a8a8a;border-radius:22px;box-shadow:none;padding:44px 40px}
.label-left{left:24px}
.label-right{left:612px}
.label-address{font-size:14px;margin-top:12px;padding-left:78px}
.label-next{top:3494px;height:60px}
</style>
</head>
<body>

<!-- Letterhead back -->
<section class="sheet letterhead-back" aria-label="Letterhead reverse">
  <div class="ghost-ring" style="left:60px;top:140px;width:420px;height:420px"></div>
  <div class="wordmark" style="position:absolute;left:90px;top:314px">
    <div class="dot" style="width:70px;height:70px"></div>
    <div class="lines"><span class="top" style="font-size:40px">KESTAVO</span><span class="bottom" style="font-size:22px">ESTATES</span></div>
  </div>
</section>

<!-- Letterhead front -->
<section class="sheet letterhead-front" aria-label="Letterhead">
  <header class="lh-header">
    <div class="wordmark">
      <div class="dot" style="width:30px;height:30px"></div>
      <div class="lines"><span class="top" style="font-size:18px">KESTAVO</span><span class="bottom" style="font-size:10px">ESTATES</span></div>
    </div>
    <div class="lh-person"><div class="name">Peter T. Vance</div><div class="title">CEO</div></div>
  </header>
  <div class="lh-body">
    <p>Lorem ipsum dolor sit amet, consectetur adipisicing elit, sed do eiusmod tempor incididunt ut labore et dolore magna aliqua. Ut enim ad minim veniam, quis nostrud exercitation ullamco laboris nisi ut aliquip ex ea commodo consequat. Duis aute irure dolor in reprehenderit in voluptate velit esse cillum dolore eu fugiat nulla pariatur. Excepteur sint occaecat cupidatat non proident, sunt in culpa qui officia deserunt mollit anim id est laborum. Sed ut perspiciatis unde omnis iste natus error sit voluptatem accusantium doloremque laudantium, totam rem aperiam, eaque ipsa quae ab illo inventore veritatis et quasi architecto beatae vitae dicta sunt explicabo. Nemo enim ipsam voluptatem quia voluptas sit aspernatur aut odit aut fugit, sed quia consequuntur magni dolores eos qui ratione voluptatem sequi nesciunt. Neque porro quisquam est, qui dolorem ipsum quia dolor sit amet, consectetur, adipisci velit, sed quia non numquam eius modi tempora incidunt ut labore et dolore magnam aliquam quaerat voluptatem.</p>
    <p>Lorem ipsum dolor sit amet, consectetur adipisicing elit, sed do eiusmod tempor incididunt ut labore et dolore magna aliqua. Ut enim ad minim veniam, quis nostrud exercitation ullamco laboris nisi ut aliquip ex ea commodo consequat. Duis aute irure dolor in reprehenderit in voluptate velit esse cillum dolore eu fugiat nulla pariatur. Excepteur sint occaecat cupidatat non</p>
  </div>
  <footer class="lh-footer">
    <strong>KESTAVO ESTATES</strong><br>
    Address : 1870 Pembrook Blvd. Suite 400, Atlanta, GA 30127<br>
    Off 770.555.0214 | Fax 770.555.0287 | Email email@kestavoestates.com<br>
    www.kestavoestates.com
  </footer>
  <div class="band-stripes"><i></i><i></i><i></i><i></i></div>
  <div class="band"></div>
</section>

<!-- Business card front -->
<section class="sheet card card-front" aria-label="Business card front">
  <div class="ghost-ring" style="left:125px;top:2px;width:270px;height:270px;border-width:22px"></div>
  <div class="wordmark" style="position:relative">
    <div class="dot" style="width:46px;height:46px"></div>
    <div class="lines"><span class="top" style="font-size:30px">KESTAVO</span><span class="bottom" style="font-size:16px">ESTATES</span></div>
  </div>
</section>

<!-- Business card back -->
<section class="sheet card card-back" aria-label="Business card contact side">
  <div class="card-name">Peter T. Vance</div>
  <div class="card-title">CEO</div>
  <div class="contact-row">
    <svg class="icon" viewBox="0 0 20 20" aria-hidden="true"><path d="M10 4a4 4 0 0 0-4 4c0 3 4 8 4 8s4-5 4-8a4 4 0 0 0-4-4zm0 5.5a1.5 1.5 0 1 1 0-3 1.5 1.5 0 0 1 0 3z" fill="#fff"/></svg>
    <span>1870 Pembrook Blvd. Suite 400, Atlanta, GA 30127</span>
  </div>
  <div class="contact-row">
    <svg class="icon" viewBox="0 0 20 20" aria-hidden="true"><path d="M6 4l2.5 3-1.5 1.5c.8 1.7 2 2.9 3.5 3.5L12 10.5l3 2.5-1.5 2.5C9 15 5 11 4.5 5.5z" fill="#fff"/></svg>
    <span>770.555.02##</span>
  </div>
  <div class="contact-row">
    <svg class="icon" viewBox="0 0 20 20" aria-hidden="true"><rect x="7" y="4" width="6" height="12" rx="1" fill="#fff"/><rect x="8" y="5.5" width="4" height="7" fill="#003e7c"/></svg>
    <span>404.555.####</span>
  </div>
  <div class="contact-row">
    <svg class="icon" viewBox="0 0 20 20" aria-hidden="true"><rect x="4" y="6" width="12" height="8" fill="#fff"/><path d="M4 6l6 5 6-5" stroke="#003e7c" fill="none"/></svg>
    <span>email@kestavoestates.com</span>
  </div>
  <div class="contact-row">
    <svg class="icon" viewBox="0 0 20 20" aria-hidden="true"><circle cx="10" cy="10" r="6" fill="none" stroke="#fff" stroke-width="1.5"/><path d="M4 10h12M10 4c-3 3-3 9 0 12M10 4c3 3 3 9 0 12" stroke="#fff" fill="none"/></svg>
    <span>www.kestavoestates.com</span>
  </div>
</section>

<!-- Envelope back -->
<section class="sheet envelope-back" aria-label="Envelope reverse">
  <svg viewBox="0 0 1008 516" preserveAspectRatio="none" aria-hidden="true">
    <path d="M0 0 L504 250 L1008 0" fill="#f7f8fa" stroke="#d9dde3" stroke-width="2"/>
    <path d="M0 516 L430 230 M1008 516 L578 230" stroke="#e1e4e9" stroke-width="2" fill="none"/>
  </svg>
  <div class="ghost-ring" style="left:414px;top:20px;width:180px;height:180px;border-width:18px"></div>
  <div class="wordmark" style="position:absolute;left:400px;top:82px">
    <div class="dot" style="width:34px;height:34px"></div>
    <div class="lines"><span class="top" style="font-size:24px">KESTAVO</span><span class="bottom" style="font-size:13px">ESTATES</span></div>
  </div>
</section>

<!-- Envelope front -->
<section class="sheet envelope-front" aria-label="No. 10 envelope">
  <div class="env-return">
    <div class="wordmark">
      <div class="dot" style="width:40px;height:40px"></div>
      <div class="lines"><span class="top" style="font-size:28px">KESTAVO</span><span class="bottom" style="font-size:15px">ESTATES</span></div>
    </div>
    <div class="env-address">1870 Pembrook Blvd. Suite 400<br>Atlanta, GA 30127</div>
  </div>
  <div class="band-stripes"><i></i><i></i><i></i><i></i></div>
  <div class="band"></div>
</section>

<!-- Shipping labels -->
<section class="sheet label label-left" aria-label="Shipping label">
  <div class="wordmark">
    <div class="dot" style="width:66px;height:66px"></div>
    <div class="lines"><span class="top" style="font-size:44px">KESTAVO</span><span class="bottom" style="font-size:22px">ESTATES</span></div>
  </div>
  <div class="label-address">1870 Pembrook Blvd. Suite 400, Atlanta, GA 30127</div>
</section>
<section class="sheet label label-right" aria-label="Shipping label">
  <div class="wordmark">
    <div class="dot" style="width:66px;height:66px"></div>
    <div class="lines"><span class="top" style="font-size:44px">KESTAVO</span><span class="bottom" style="font-size:22px">ESTATES</span></div>
  </div>
  <div class="label-address">1870 Pembrook Blvd. Suite 400, Atlanta, GA 30127</div>
</section>
<div class="sheet label label-left label-next" aria-hidden="true"></div>
<div class="sheet label label-right label-next" aria-hidden="true"></div>

</body>
</html>
```